Personal Business Card

I am an award winning banjo player who plays with two different professional bands. My experiences include studio recordings for other artists and played the theme song for the Creature Channel's "Frontier Tundra Trails". I am ready to take my career to the next level and would like something that will look professional. it is important to me to have a banjo on the card. If possible my accomplishments to be put on back of card.

Industry/Entity Type

Artists

Contact Information for Business Card

Corbin Halloway
cell 602-315-2860
email corbinhallowaybanjo@mailvista.net

2008 AZ Banjo Champion
2008 Pinebrook Banjo Champion
2010 AZ Banjo Champion
2010 Riverbend Hoedown Talcott Banjo Champion
2010 Cedar Hollow Gathering Banjo Finalist

```html
<!DOCTYPE html>
<html lang="en">
<head>
<meta charset="utf-8">
<title>Corbin Halloway – Business Card</title>
<link href="https://fonts.googleapis.com/css2?family=Almendra:wght@400;700&family=Archivo:wght@600;700;800&display=swap" rel="stylesheet">
<style>
  :root {
    --mustard: #f0b84a;
    --mustard-deep: #e3a93a;
    --ink: #1b1b1b;
    --paper: #ffffff;
    --table: #e8e5df;
    --sketch: #d9d9d9;
    --sketch-soft: #f1f1f1;
  }
  * { box-sizing: border-box; margin: 0; padding: 0; }
  html, body { width: 1200px; height: 900px; overflow: hidden; }
  body {
    background: var(--table);
    font-family: "Archivo", Arial, sans-serif;
    color: var(--ink);
    position: relative;
  }
  .card {
    position: absolute;
    left: 250px;
    width: 700px;
    height: 400px;
    background: var(--paper);
    box-shadow: 0 6px 18px rgba(0,0,0,.18);
    overflow: hidden;
  }
  .card--back { top: 30px; }
  .card--front { top: 470px; }

  /* Front */
  .front-band {
    position: absolute; left: 0; top: 0; bottom: 0; width: 300px;
    background: var(--mustard);
  }
  .banjo-art {
    position: absolute; left: 40px; top: 30px; width: 230px; height: 340px;
    background: linear-gradient(160deg, var(--mustard) 0%, var(--mustard-deep) 55%, #fff3d8 100%);
    border-radius: 8px;
  }
  .front-info { position: absolute; left: 340px; top: 34px; right: 30px; }
  .name { font-family: "Almendra", Georgia, serif; font-weight: 700; line-height: .95; }
  .name__first { display: block; font-size: 62px; color: var(--ink); }
  .name__last { display: block; font-size: 58px; color: var(--mustard); padding-left: 70px; }
  .contact { margin-top: 24px; }
  .contact__label { display: block; color: var(--mustard); font-weight: 700; font-size: 21px; line-height: 1.1; }
  .contact__value { display: block; font-weight: 700; font-size: 20px; margin-bottom: 10px; white-space: nowrap; }
  .contact__value--email { font-size: 17.5px; }

  /* Back */
  .back-strip {
    position: absolute; left: 0; top: 0; bottom: 0; width: 120px;
    background: var(--mustard);
  }
  .back-strip__name {
    position: absolute; left: 14px; top: 20px; height: 360px;
    writing-mode: vertical-rl; transform: rotate(180deg);
    font-family: "Almendra", Georgia, serif; font-weight: 700;
    font-size: 34px; color: var(--ink); text-align: center;
  }
  .year {
    position: absolute; left: 70px;
    writing-mode: vertical-rl; transform: rotate(180deg);
    color: var(--paper); font-weight: 800; font-size: 24px; letter-spacing: 1px;
  }
  .year--2008 { top: 60px; }
  .year--2010 { top: 215px; }
  .banjo-sketch {
    position: absolute; right: 0; top: 0; width: 380px; height: 230px;
    background: radial-gradient(ellipse at 80% 75%, var(--sketch) 0%, var(--sketch-soft) 45%, var(--paper) 80%);
  }
  .awards { position: absolute; left: 150px; top: 60px; list-style: none; }
  .awards li { font-weight: 800; font-size: 21px; line-height: 1.45; }
  .awards li.group-start { margin-top: 36px; }
</style>
</head>
<body>

<section class="card card--back" aria-label="Back of card">
  <div class="back-strip">
    <div class="back-strip__name">Corbin Halloway</div>
    <span class="year year--2008">2008</span>
    <span class="year year--2010">2010</span>
  </div>
  <div class="banjo-sketch" role="img" aria-label="Faint line sketch of a banjo"></div>
  <ul class="awards">
    <li>AZ Banjo Champion</li>
    <li>Pinebrook Banjo Champion</li>
    <li class="group-start">AZ Banjo Champion</li>
    <li>Riverbend Hoedown Talcott Banjo Champion</li>
    <li>Cedar Hollow Gathering Banjo Finalist</li>
  </ul>
</section>

<section class="card card--front" aria-label="Front of card">
  <div class="front-band">
    <div class="banjo-art" role="img" aria-label="Hand-drawn banjo illustration"></div>
  </div>
  <div class="front-info">
    <h1 class="name">
      <span class="name__first">Corbin</span>
      <span class="name__last">Halloway</span>
    </h1>
    <div class="contact">
      <span class="contact__label">cell</span>
      <span class="contact__value">602-315-2860</span>
      <span class="contact__label">e-mail</span>
      <span class="contact__value contact__value--email">corbinhallowaybanjo@mailvista.net</span>
    </div>
  </div>
</section>

</body>
</html>
```